Lumo Quest - Main Menu - Re-Design

I want to have a refresh for this app's main menu. There are some different items on the menu depending on the language (English vs. Non-English) and version (Pro vs. Free). I have attached screenshots of the different conditions. This app is a collection of brain training games.

Need designs for light and dark mode. Need designs for both portrait and landscape mode.

Here is a link to the app in Vexo Shelf.
https://shelf.vexomarket.test/store/apps/details?id=tarnwick.lumoquest

Here is a link to the app in the Quorra App Depot.
https://apps.quorradepot.test/us/app/lumo-quest-brain-training/id573918204?ls=1&mt=8

```html
<!DOCTYPE html>
<html lang="en">
<head>
<meta charset="UTF-8">
<title>Lumo Quest – Main Menu</title>
<link rel="stylesheet" href="https://fonts.googleapis.com/css2?family=Rubik:wght@400;500;700;800&display=swap">
<style>
  :root {
    --bg: #000000;
    --header-glow: #0c2a33;
    --text: #ffffff;
    --muted: #a9a9a9;
    --banner: #17160f;
    --banner-bottom: #141413;
    --card-game: #441616;
    --card-game-top: #4c1a1c;
    --card-training: #033637;
    --card-training-top: #053c3f;
    --card-upgrade: #18232b;
    --card-plain: #1c1c1b;
    --icon-blue: #3d8fdf;
    --icon-calendar: #e9ecef;
    --icon-calendar-top: #e8584a;
    --icon-gear: #4f7bb3;
  }
  * { box-sizing: border-box; margin: 0; padding: 0; }
  html, body { width: 675px; height: 1200px; overflow: hidden; background: var(--bg); }
  body { font-family: "Rubik", sans-serif; color: var(--text); position: relative; }

  .menu { position: relative; width: 675px; height: 1200px;
    background: radial-gradient(ellipse 420px 260px at 440px 40px, var(--header-glow), transparent 75%), var(--bg); }

  .header-art { position: absolute; left: 378px; top: 0; width: 172px; height: 144px;
    border-radius: 0 0 60px 60px;
    background: linear-gradient(90deg, #34402a 0 49%, transparent 49% 51%, #0f3a55 51%); opacity: .8; }
  .info { position: absolute; left: 611px; top: 37px; width: 26px; height: 26px; }

  .welcome { position: absolute; left: 31px; top: 68px; font-size: 20px; font-weight: 700; }
  .progress { position: absolute; left: 31px; top: 108px; font-size: 16px; font-weight: 400; }
  .progress b { font-weight: 500; margin: 0 5px; }

  .card { position: absolute; border-radius: 19px; }
  .feature { top: 197px; width: 297px; height: 228px; }
  .feature .title { position: absolute; left: 37px; top: 31px; font-size: 23px; font-weight: 800; }
  .feature .sub { position: absolute; left: 37px; top: 70px; font-size: 14px; font-weight: 400; }
  .game-list { left: 31px; background: linear-gradient(160deg, var(--card-game-top), var(--card-game)); }
  .training { left: 347px; background: linear-gradient(160deg, var(--card-training-top), var(--card-training)); }
  .art { position: absolute; }
  .game-list .art { left: 172px; top: 106px; width: 94px; height: 100px; border-radius: 40px 40px 30px 30px;
    background: linear-gradient(170deg, #3a2e4a 0 30%, #f9c846 30%); }
  .training .art { left: 167px; top: 108px; width: 98px; height: 98px; border-radius: 30px;
    background: linear-gradient(180deg, #5fd7d0 0 40%, #f3a3ad 40% 80%, #4d5560 80%); }

  .banner { position: absolute; left: 0; width: 675px; background: var(--banner);
    display: flex; align-items: center; justify-content: center; font-size: 22px; color: var(--muted); }
  .banner.top { top: 466px; height: 140px; }
  .banner.bottom { top: 1059px; height: 141px; background: var(--banner-bottom); }

  .tile { width: 297px; height: 109px; display: flex; align-items: center; }
  .tile .label { position: absolute; left: 38px; font-size: 19px; font-weight: 800; }
  .tile .icon { position: absolute; left: 206px; top: 28px; width: 53px; height: 53px; }
  .col-l { left: 31px; } .col-r { left: 347px; }
  .row-1 { top: 637px; } .row-2 { top: 778px; } .row-3 { top: 919px; }
  .upgrade { background: var(--card-upgrade); }
  .apps { background: linear-gradient(110deg, #3a0d1f, #2b0518); }
  .plain { background: linear-gradient(100deg, #1f1f1c, #181818); }

  .icon.arrow-badge { border-radius: 50%; background: var(--icon-blue); }
  .icon.cubes { border-radius: 8px; background: linear-gradient(135deg, #f0327a 0 35%, #28d3d8 35% 65%, #f9cf3b 65%); }
  .icon.book { border-radius: 10px; background: linear-gradient(180deg, #f4a0a8 0 60%, #e45a3f 60%); }
  .icon.trophy { border-radius: 12px 12px 6px 6px; background: linear-gradient(180deg, #f5b942 0 70%, #2f4a63 70%); }
  .icon.calendar { border-radius: 8px; background: linear-gradient(180deg, var(--icon-calendar-top) 0 24%, var(--icon-calendar) 24%); }
  .icon.gear { border-radius: 50%; background: var(--icon-gear); }
</style>
</head>
<body>
<main class="menu">
  <div class="header-art" role="img" aria-label="Brain illustration, half olive and half blue"></div>
  <svg class="info" viewBox="0 0 26 26" aria-label="Info">
    <circle cx="13" cy="13" r="13" fill="#fff"/>
    <circle cx="14" cy="7.5" r="1.8" fill="#000"/>
    <path d="M11 11.5h3.6l-1.6 7.5h1.8" stroke="#000" stroke-width="2.4" fill="none" stroke-linecap="round"/>
  </svg>

  <h1 class="welcome">Welcome Guest</h1>
  <p class="progress">You have finished<b>2</b>Trainings Today</p>

  <section class="card feature game-list">
    <h2 class="title">Game List</h2>
    <p class="sub">Choose a Game to Play</p>
    <div class="art" role="img" aria-label="Yellow game controller illustration"></div>
  </section>
  <section class="card feature training">
    <h2 class="title">Training Center</h2>
    <p class="sub">Start Today’s Training</p>
    <div class="art" role="img" aria-label="Brain lifting a barbell illustration"></div>
  </section>

  <div class="banner top">Banner Ad</div>

  <section class="card tile upgrade col-l row-1">
    <span class="label">Upgrade</span>
    <div class="icon arrow-badge" role="img" aria-label="Blue upgrade badge illustration"></div>
  </section>
  <section class="card tile apps col-r row-1">
    <span class="label">More Apps</span>
    <div class="icon cubes" role="img" aria-label="Stacked colourful cubes illustration"></div>
  </section>

  <section class="card tile plain col-l row-2">
    <span class="label">Learning</span>
    <div class="icon book" role="img" aria-label="Brain above an open book illustration"></div>
  </section>
  <section class="card tile plain col-r row-2">
    <span class="label">Scores</span>
    <div class="icon trophy" role="img" aria-label="Gold trophy illustration"></div>
  </section>

  <section class="card tile plain col-l row-3">
    <span class="label">Schedule</span>
    <div class="icon calendar" role="img" aria-label="Calendar illustration"></div>
  </section>
  <section class="card tile plain col-r row-3">
    <span class="label">Settings</span>
    <div class="icon gear" role="img" aria-label="Blue settings gear illustration"></div>
  </section>

  <div class="banner bottom">Banner Ad</div>
</main>
</body>
</html>
```